Real Estate investment company needs billboard designs

This is our website: https://velmarkpropertygroup.com/
We are looking for some billboard concepts that uses our CEO in the design. I have attached some images and 1 billboard design that someone in our industry uses, but we don't want it exactly like his.

Industry/Entity Type

real estate

Colors

Designer to choose colors to be used in the design.

Requirements
Must have
• Company colors from websiute

```html
<!DOCTYPE html>
<html lang="en">
<head>
<meta charset="UTF-8">
<title>Velmark Property Group – Billboard</title>
<link rel="stylesheet" href="https://fonts.googleapis.com/css2?family=Anton&family=Montserrat:wght@700;800&family=Oswald:wght@600&display=swap">
<style>
  :root {
    --navy: #1b1a3a;
    --red: #fb1111;
    --white: #ffffff;
    --stage: #eef0f3;
    --photo-light: #dfe8f2;
    --photo-mid: #a9bfd8;
  }
  html, body {
    margin: 0;
    padding: 0;
    width: 982px;
    height: 1200px;
    overflow: hidden;
    background: var(--stage);
  }
  .billboard {
    position: absolute;
    left: 0;
    top: 373px;
    width: 982px;
    height: 453px;
    display: block;
  }
  .headline-main { font-family: "Anton", sans-serif; fill: var(--navy); }
  .headline-sub  { font-family: "Anton", sans-serif; fill: var(--red); }
  .brand-name    { font-family: "Montserrat", sans-serif; font-weight: 800; fill: var(--navy); }
  .website       { font-family: "Montserrat", sans-serif; font-weight: 700; fill: var(--white); }
  .phone-number  { font-family: "Oswald", sans-serif; font-weight: 600; fill: var(--white); }
</style>
</head>
<body>
<svg class="billboard" viewBox="0 0 982 453" xmlns="http://www.w3.org/2000/svg">
  <defs>
    <linearGradient id="ceo-tone" x1="0" y1="0" x2="0" y2="1">
      <stop offset="0" stop-color="#dfe8f2"/>
      <stop offset="1" stop-color="#a9bfd8"/>
    </linearGradient>
  </defs>

  <rect class="billboard-bg" x="0" y="0" width="982" height="453" fill="var(--white)"/>

  <g class="ceo-portrait" role="img" aria-label="Photo of the company CEO in a light blue denim shirt, pointing toward the headline">
    <rect x="0" y="14" width="400" height="358" fill="url(#ceo-tone)"/>
  </g>

  <text class="headline-main" x="420" y="172" font-size="170" textLength="540" lengthAdjust="spacingAndGlyphs">SELLING</text>
  <text class="headline-sub" x="424" y="280" font-size="100" textLength="500" lengthAdjust="spacingAndGlyphs">YOUR HOME?</text>

  <g class="brand">
    <rect x="690" y="312" width="16" height="16" fill="var(--red)"/>
    <text class="brand-name" x="714" y="329" font-size="26" textLength="188" lengthAdjust="spacingAndGlyphs">VELMARK</text>
    <text class="brand-name" x="714" y="356" font-size="14" textLength="188" lengthAdjust="spacingAndGlyphs">PROPERTY GROUP</text>
  </g>

  <polygon class="phone-band" points="0,372 529,372 569,453 0,453" fill="var(--navy)"/>
  <polygon class="web-band" points="553,412 982,412 982,453 573,453" fill="var(--red)"/>

  <g class="phone-icon">
    <circle cx="60" cy="414" r="30" fill="var(--white)"/>
    <path d="M48 399 l6 -2 l6 10 l-5 4 c2 6 6 10 12 12 l4 -5 l10 6 l-2 6 c-1 3 -4 4 -7 4 c-14 -3 -25 -14 -28 -28 c0 -3 1 -6 4 -7 z" fill="var(--navy)"/>
    <path d="M64 400 a10 10 0 0 1 10 10 M65 393 a17 17 0 0 1 16 16" fill="none" stroke="var(--navy)" stroke-width="3" stroke-linecap="round"/>
  </g>

  <text class="phone-number" x="106" y="444" font-size="78" textLength="388" lengthAdjust="spacingAndGlyphs">555.214.7390</text>

  <text class="website" x="600" y="441" font-size="21" textLength="355" lengthAdjust="spacingAndGlyphs">velmarkpropertygroup.com</text>
</svg>
</body>
</html>
```